WXO Business Card Design

Business card design per the attached files.

Target Market(s)

Government and military officials, aerospace companies and aviation professionals

Industry/Entity Type

Business

```html
<!DOCTYPE html>
<html lang="en">
<head>
<meta charset="utf-8">
<title>WXO Business Card</title>
<link href="https://fonts.googleapis.com/css2?family=Open+Sans:wght@400;600;700;800&display=swap" rel="stylesheet">
<style>
  :root {
    --backdrop: #e4e4e6;
    --ink: #0b0b0c;
    --paper: #f1f1f0;
    --blue: #1a8fd6;
    --grey: #8c8c8c;
    --white: #ffffff;
    --text-dark: #1d1d1d;
  }
  * { box-sizing: border-box; margin: 0; padding: 0; }
  html, body {
    width: 1200px; height: 675px; overflow: hidden;
    background: var(--backdrop);
    font-family: "Open Sans", Arial, sans-serif;
  }
  .canvas {
    position: relative; width: 1200px; height: 675px;
    display: flex; align-items: center; justify-content: center; gap: 60px;
  }
  .card {
    position: relative; width: 520px; height: 297px; overflow: hidden;
    box-shadow: 0 6px 18px rgba(0,0,0,.18);
  }

  /* Front */
  .card-front { background: var(--ink); }
  .front-brand {
    position: absolute; top: 82px; left: 0; right: 0;
    display: flex; align-items: center; justify-content: center; gap: 12px;
  }
  .brand-name {
    font-weight: 800; font-size: 52px; letter-spacing: 2px;
    color: var(--white); line-height: 1;
  }
  .brand-dot {
    width: 12px; height: 12px; border-radius: 50%;
    background: var(--blue);
  }
  .tagline-band {
    position: absolute; left: 0; right: 0; top: 190px; height: 36px;
    background: var(--blue);
    display: flex; align-items: center; justify-content: center;
  }
  .tagline {
    color: var(--white); font-size: 16px; letter-spacing: 4px; font-weight: 400;
  }

  /* Back */
  .card-back { background: var(--paper); }
  .globe-art {
    position: absolute; left: 30px; top: 96px; width: 250px; height: 250px;
    border-radius: 50%;
    background: radial-gradient(circle at 45% 40%, #d7d7d7 0%, #a6a6a6 55%, #4b4b4b 85%, #1f4a9c 100%);
  }
  .back-brand {
    position: absolute; top: 34px; right: 42px; text-align: right;
  }
  .back-brand .brand-row { display: flex; align-items: center; gap: 8px; justify-content: flex-end; }
  .back-brand .brand-name { color: var(--text-dark); font-size: 34px; letter-spacing: 1px; }
  .back-brand .brand-dot { width: 8px; height: 8px; }
  .division { font-size: 10px; font-weight: 700; color: var(--text-dark); margin-top: 2px; }
  .person {
    position: absolute; top: 108px; right: 42px; text-align: right;
  }
  .person-name { color: var(--blue); font-weight: 700; font-size: 14px; }
  .person-role { color: var(--grey); font-size: 7px; letter-spacing: 1px; margin-top: 1px; }
  .person-phone { font-size: 10px; font-weight: 600; color: var(--text-dark); margin-top: 3px; }
  .contact-band {
    position: absolute; right: 0; top: 158px; width: 330px; height: 96px;
    background: var(--ink);
    clip-path: polygon(12% 0, 100% 0, 100% 100%, 0 100%, 0 45%);
    padding: 12px 36px 0 0; text-align: right;
  }
  .contact-line {
    display: flex; justify-content: flex-end; align-items: center; gap: 6px;
    color: var(--white); font-size: 9.5px; line-height: 15px;
  }
  .contact-line.accent { color: var(--blue); font-weight: 600; }
  .icon { width: 9px; height: 9px; flex: none; }
  .icon-inline { display: inline-flex; align-items: center; gap: 5px; }
</style>
</head>
<body>
<main class="canvas">

  <section class="card card-front" aria-label="Card front">
    <div class="front-brand">
      <span class="brand-name">VANTAGE</span>
      <span class="brand-dot"></span>
    </div>
    <div class="tagline-band">
      <span class="tagline">READY • CAPABLE • CONNECTED</span>
    </div>
  </section>

  <section class="card card-back" aria-label="Card back">
    <div class="globe-art" role="img" aria-label="Illustration of a wireframe globe circled by blue orbit rings and aircraft"></div>

    <div class="back-brand">
      <div class="brand-row">
        <span class="brand-name">VANTAGE</span>
        <span class="brand-dot"></span>
      </div>
      <div class="division">Nordlys Air Ehf</div>
    </div>

    <div class="person">
      <div class="person-name">Einar K. Sigurdsson</div>
      <div class="person-role">PRINCIPAL</div>
      <div class="person-phone icon-inline">+354 555 0142
        <svg class="icon" viewBox="0 0 10 10"><rect x="2.5" y="0.5" width="5" height="9" rx="1" fill="none" stroke="#1a8fd6" stroke-width="1"/></svg>
      </div>
    </div>

    <div class="contact-band">
      <div class="contact-line accent">+354 555 0187
        <svg class="icon" viewBox="0 0 10 10"><path d="M2 1 L4 1 L4.6 3.2 L3.5 4 Q4.5 6 6 6.5 L6.8 5.4 L9 6 L9 8 Q5 9.5 1 3 Z" fill="#1a8fd6"/></svg>
      </div>
      <div class="contact-line">
        <span class="icon-inline">
          <svg class="icon" viewBox="0 0 10 10"><rect x="0.5" y="2" width="9" height="6" fill="#fff"/><path d="M0.5 2 L5 5.5 L9.5 2" fill="none" stroke="#0b0b0c" stroke-width="0.8"/></svg>
          www.wxo.is
        </span>
        <svg class="icon" viewBox="0 0 10 10"><circle cx="5" cy="5" r="4" fill="none" stroke="#fff" stroke-width="1"/><path d="M1 5 H9 M5 1 Q2.5 5 5 9 M5 1 Q7.5 5 5 9" fill="none" stroke="#fff" stroke-width="0.7"/></svg>
      </div>
      <div class="contact-line">einar@wxo.is</div>
      <div class="contact-line">Hafnargata 12 101 Reykjavik Iceland</div>
    </div>
  </section>

</main>
</body>
</html>
```